Postcard Design

Company Name--motion harbor
482 Garnet Avenue
Brooklyn New York11231
347-555-0182
www.motionharbors. example
We are a boutique personal fitness company in a exclusive neighnorhood in Brooklyn New York. We specialize in personal training and innovate new fitness classes such as Pulse-Circuit QVR and Tabata.

We want our brand to be high-end but open to all. Laid-back but experts in the field of fitness. Innovative and flexible. Proffessional, friendly and inspiring.

Personal attention for our clients is a must as well as making sure they succeed. 87% of our clients reach their goals.

Colors should be bright but sophisticated with a little aggression but not intimidation.
Updates

Company Name-And contact info has been updated on the brief

I posted a logo. And the colors on the website have changed. If you could incorporate the website color scheme that would be helpful. If for whatever reason the logo is not here I will try to upload again.

Change the contact info: www.motionharbors.example You tube: Brisco and the Motion Harbor Email: Motionharbors@mailbox.example Verbiage changes: 'The only boutique personal fitness studio in Brooklyn. Featuring uniquely proprietary classes QVR, Cross Training and now Tabata." Verbiage Additions Safe for moms, dads and we offer enhanced childcare with certified child care development teachers with our partner studios. Classes start at $15

Please Add : Use this postcard to receive 10% any service

Hi, I could not upload the logo. However they said that our Logo should be uploaded now as I sent it to them manually.

Target Market(s)

30-40 year old women and new moms looking to do cross fit and personal training. Income 80-85K.

Industry/Entity Type

Boutique

Requirements
Must have
• Highlight Tabata and the excellence of the classes.Tag lines- Increase calorie burn by 20%. Increase muscle tone by 25%.Increase metabolism by 25%. Classes only available by appointment. 30mins or 1 hour.
Nice to have
• Attractive and fit young people having fun. Personal training.
Should not have
• Overly sexual fitness models.

```html
<!DOCTYPE html>
<html lang="en">
<head>
<meta charset="utf-8">
<title>Motion Harbor Postcard</title>
<link href="https://fonts.googleapis.com/css2?family=Roboto+Condensed:ital,wght@0,400;0,700;0,800;1,800&display=swap" rel="stylesheet">
<style>
  :root {
    --stage: #5e5f61;
    --card: #ffffff;
    --ink: #231f20;
    --red: #d5232f;
    --yellow: #fff200;
    --panel: #231f20;
    --white: #ffffff;
    --skin: #e2b795;
    --hair: #9a5a32;
    --floor: #e4ebf1;
  }
  * { margin: 0; padding: 0; box-sizing: border-box; }
  html, body {
    width: 1200px; height: 962px; overflow: hidden;
    background: var(--stage);
    font-family: "Roboto Condensed", "Arial Narrow", sans-serif;
    color: var(--ink);
  }
  .postcard {
    position: absolute; left: 82px; top: 83px;
    width: 1036px; height: 795px;
    background: var(--card);
    overflow: hidden;
  }
  .postcard > * { position: absolute; }
  .hero-photo {
    left: 340px; top: 72px; width: 696px; height: 540px;
    background:
      linear-gradient(180deg, rgba(255,255,255,0) 70%, var(--floor) 100%),
      linear-gradient(100deg, rgba(226,183,149,0) 10%, rgba(226,183,149,0.35) 40%, rgba(154,90,50,0.45) 72%, rgba(226,183,149,0.35) 100%),
      var(--card);
    -webkit-mask-image: linear-gradient(90deg, transparent 0%, #000 22%, #000 100%);
    mask-image: linear-gradient(90deg, transparent 0%, #000 22%, #000 100%);
  }
  .intro {
    left: 46px; top: 28px;
    font-size: 35px; font-weight: 700; line-height: 43px;
  }
  .class-list {
    left: 46px; top: 126px;
    color: var(--red); font-size: 48px; font-weight: 700;
    line-height: 54px; text-transform: uppercase;
  }
  .featured-class {
    left: 40px; top: 232px;
    color: var(--red); font-size: 112px; font-weight: 800;
    line-height: 112px; letter-spacing: -1px;
    transform: scaleX(0.86); transform-origin: left top;
  }
  .audience {
    left: 46px; top: 373px;
    font-size: 21px; font-weight: 400; line-height: 25px;
  }
  .offer { left: 40px; top: 538px; }
  .offer-lead { font-size: 23px; font-weight: 400; line-height: 26px; text-transform: uppercase; }
  .offer-deal { color: var(--red); font-size: 35px; font-weight: 700; line-height: 38px; text-transform: uppercase; }
  .price-badge {
    left: 486px; top: 157px; width: 200px; height: 200px;
    border-radius: 50%; background: var(--red);
    border: 5px solid var(--white);
    color: var(--white); text-align: center;
  }
  .price-label {
    position: absolute; left: 0; right: 0; top: 26px;
    font-size: 28px; font-weight: 700; line-height: 28px;
    transform: rotate(12deg); text-transform: uppercase;
  }
  .price-amount {
    position: absolute; left: 0; right: 0; top: 84px;
    color: var(--yellow); font-size: 80px; font-weight: 800; line-height: 80px;
    transform: rotate(-6deg);
  }
  .price-amount sup { font-size: 38px; vertical-align: 22px; }
  .register-panel {
    left: 34px; top: 627px; width: 660px; height: 116px;
    background: var(--panel); border-radius: 12px;
    color: var(--white); padding: 16px 0 0 44px;
    font-style: italic; font-weight: 800;
  }
  .register-title { font-size: 44px; line-height: 48px; text-transform: uppercase; }
  .register-contacts { margin-top: 4px; font-size: 27px; line-height: 32px; text-transform: uppercase; white-space: nowrap; }
  .register-contacts .bullet {
    display: inline-block; width: 12px; height: 12px;
    background: var(--yellow); margin: 0 6px 0 0; vertical-align: 3px;
  }
  .register-contacts .gap { margin-left: 12px; }
  .brand-box {
    left: 724px; top: 623px; width: 276px; height: 124px;
    border: 3px solid var(--ink);
    display: flex; flex-direction: column; justify-content: center; align-items: center;
    font-size: 44px; font-weight: 700; line-height: 46px; text-transform: uppercase;
    color: var(--ink);
  }
  .footer-line {
    left: 42px; top: 757px; width: 990px;
    font-size: 19px; line-height: 22px; white-space: nowrap;
  }
  .footer-line strong { font-weight: 700; }
  .footer-line .brand-name { margin-right: 18px; text-transform: uppercase; }
  .footer-line .label { margin-right: 4px; }
  .footer-line .sep {
    display: inline-block; width: 9px; height: 9px;
    background: var(--red); margin: 0 10px; vertical-align: 2px;
  }
</style>
</head>
<body>
  <main class="postcard">
    <div class="hero-photo" role="img" aria-label="Photo of a woman in a white tank top doing a push-up on a light floor"></div>

    <h1 class="intro">The only boutique personal fitness studio in Brooklyn.<br>Featuring uniquely proprietary classes</h1>

    <p class="class-list">QVR, Cross Training<br>&amp; Now</p>
    <p class="featured-class">TABATA</p>

    <p class="audience">Safe for moms, dads and we offer<br>enhanced childcare with certified<br>child care development teachers<br>with our partner studios.</p>

    <div class="offer">
      <p class="offer-lead">Use this postcard to receive</p>
      <p class="offer-deal">10% off on any service</p>
    </div>

    <div class="price-badge">
      <p class="price-label">Classes<br>start at</p>
      <p class="price-amount"><sup>$</sup>15</p>
    </div>

    <div class="register-panel">
      <p class="register-title">Register today!!</p>
      <p class="register-contacts"><span class="bullet"></span>347-555-0182<span class="gap"></span><span class="bullet"></span>www.motionharbors.example</p>
    </div>

    <div class="brand-box">
      <span>Motion</span>
      <span>Harbor</span>
    </div>

    <p class="footer-line"><strong class="brand-name">Motion Harbor</strong>482 Garnet Avenue Brooklyn New York11231<span class="sep"></span><strong class="label">P:</strong>347-555-0182<span class="sep"></span><strong class="label">E:</strong>Motionharbors@mailbox.example</p>
  </main>
</body>
</html>
```